Stationary For Commercial Real Estate Company

We need a consistently branded image for our business cards, letterhead, property marketing flyers, powerpoint presentations, etc.

We are a COMMERCIAL real estate company. We do NOT do residential real estate, so please do not submit any designs with references to houses as they will be rejected.

We just completed a design contest for our logo, so we want to encorporate that logo in our stationary design, and we have attached it for your use. Please let us know if you need the logo in another format.

We can accept the business cards in adobe illustrator, the letterhead needs to be a template in Microsoft Word, the Property Flyer can be either in PowerPoint or Adobe Illustrator, and the PowerPoint presentation needs to have a Cover Page, Table of Contents, a few sample pages, and a Closing/Summary slide at the end.

We have attached a sample Property Flyer to show what we are basically looking for; but this is only provided as a sample, so you can see the kind of information we generally need to include on our Flyers. They can be in either landscape or portrait layout.

Target Market(s)

CEO and Upper Level managers who are decision makers regarding commercial real estate projects. Local, regional and fortune 500 clients.

Industry/Entity Type

Real Estate

Requirements
Must have
• There must be a space on the Flyer that includes the disclaimer shown on the bottom of the attached sample.
Nice to have
• I appreciate the designs submitted so far, but I'd prefer not to have watermarks on the letterhead or business cards. I'm not sure I'm a big fan of the watermarks.

Also, I'd like to see some color combinations that use something other than just red. I'd like to see something where we have just the logo in red and use other contrasting colors on the letterhead or business cards.
Should not have
• Please, no references to houses or anything else that suggests residential real estate. We only do commercial real estate.

```html
<!DOCTYPE html>
<html lang="en">
<head>
<meta charset="utf-8">
<title>Halbrook Marsh Commercial Real Estate – Stationery</title>
<link href="https://fonts.googleapis.com/css2?family=Archivo:wght@400;700&family=Didact+Gothic&display=swap" rel="stylesheet">
<style>
  :root {
    --brand-red: #b4232b;
    --card-red: #a42329;
    --ink: #1b1b1b;
    --muted: #6f6f6f;
    --label-blue: #5b86a6;
    --paper: #ffffff;
    --backdrop: #e7e4e0;
    --fan-warm: #f1c8bd;
    --fan-cool: #bfe0e0;
  }
  * { margin: 0; padding: 0; box-sizing: border-box; }
  html, body { width: 1200px; height: 898px; overflow: hidden; }
  body {
    position: relative;
    background: var(--backdrop);
    font-family: "Didact Gothic", "Century Gothic", sans-serif;
    color: var(--ink);
  }

  .sheet { position: absolute; background: var(--paper); overflow: hidden; }
  .letterhead { left: 40px; top: 22px; width: 600px; height: 852px; }
  .card { width: 450px; height: 258px; }
  .card--back { left: 705px; top: 200px; background: var(--card-red); }
  .card--front { left: 705px; top: 520px; }

  .fan { position: absolute; top: 0; right: 0; }

  .brand { position: absolute; }
  .brand__mark { display: block; background: var(--brand-red); }
  .brand__name {
    font-family: "Archivo", Arial, sans-serif;
    font-weight: 700;
    text-transform: uppercase;
    line-height: 1.05;
    color: var(--ink);
  }
  .brand__tagline {
    font-family: "Archivo", Arial, sans-serif;
    font-weight: 700;
    text-transform: uppercase;
    color: var(--ink);
  }

  .letterhead .brand { left: 74px; top: 46px; }
  .letterhead .brand__mark { width: 40px; height: 40px; margin-bottom: 34px; }
  .letterhead .brand__name { font-size: 18px; }
  .letterhead .brand__tagline { font-size: 10.5px; }

  .web {
    position: absolute;
    font-size: 10px;
    color: #9a9a9a;
  }
  .letterhead .web { left: 270px; top: 44px; }

  .contact {
    position: absolute;
    display: grid;
    grid-template-columns: auto auto;
    column-gap: 22px;
    font-size: 10.5px;
    line-height: 1.15;
    color: #444;
  }
  .contact dt { color: var(--label-blue); }
  .contact dd { color: #555; }
  .letterhead .contact { left: 270px; top: 748px; }

  .card--back .brand { left: 112px; top: 70px; }
  .card--back .brand__mark { width: 44px; height: 44px; background: var(--paper); margin-bottom: 24px; margin-left: 0; }
  .card--back .brand__name { color: var(--paper); font-size: 18px; }
  .card--back .brand__tagline { color: var(--paper); font-size: 12px; }

  .card--front .brand { left: 44px; top: 36px; }
  .card--front .brand__mark { width: 34px; height: 34px; margin-bottom: 22px; }
  .card--front .brand__name { font-size: 15px; }
  .card--front .brand__tagline { font-size: 9.5px; }
  .card--front .web { left: 206px; top: 160px; font-size: 9px; }

  .person { position: absolute; left: 40px; top: 164px; }
  .person__name {
    font-family: "Archivo", Arial, sans-serif;
    font-weight: 700;
    font-size: 20px;
    color: var(--brand-red);
  }
  .person__role { font-size: 14px; color: #555; }
  .card--front .contact { left: 204px; top: 182px; font-size: 9.5px; column-gap: 16px; }
</style>
</head>
<body>

<section class="sheet letterhead" aria-label="Letterhead">
  <svg class="fan" width="380" height="520" viewBox="0 0 380 520" role="img" aria-label="Soft fan of translucent warm and cool shards spreading from the top right corner">
    <defs>
      <linearGradient id="fanLetter" x1="0" y1="0" x2="1" y2="1">
        <stop offset="0" stop-color="var(--fan-warm)" stop-opacity="0.7"/>
        <stop offset="1" stop-color="var(--fan-cool)" stop-opacity="0.15"/>
      </linearGradient>
    </defs>
    <polygon points="380,0 60,0 0,520 380,200" fill="url(#fanLetter)" opacity="0.55"/>
  </svg>
  <div class="brand">
    <span class="brand__mark"></span>
    <p class="brand__name">Halbrook Marsh</p>
    <p class="brand__tagline">Commercial Real Estate</p>
  </div>
  <p class="web">www.halbrookmarshrealestate.com</p>
  <dl class="contact">
    <dt>Mobile:</dt><dd>(01) 12345678</dd>
    <dt>Tel:</dt><dd>(01) 12345678</dd>
    <dt>email:</dt><dd>email@halbrookmarsh.com</dd>
    <dt>Address:</dt><dd>Address name 1234Address line 2 01234<br>State, Region, Country</dd>
  </dl>
</section>

<section class="sheet card card--back" aria-label="Business card back">
  <svg class="fan" width="300" height="258" viewBox="0 0 300 258" role="img" aria-label="Lighter red translucent shards fanning from the top right corner">
    <defs>
      <linearGradient id="fanRed" x1="1" y1="0" x2="0" y2="1">
        <stop offset="0" stop-color="#d8353c" stop-opacity="0.8"/>
        <stop offset="1" stop-color="#c02b32" stop-opacity="0"/>
      </linearGradient>
    </defs>
    <polygon points="300,0 40,0 60,258 300,258" fill="url(#fanRed)"/>
  </svg>
  <div class="brand">
    <span class="brand__mark"></span>
    <p class="brand__name">Halbrook Marsh</p>
    <p class="brand__tagline">Commercial Real Estate</p>
  </div>
</section>

<section class="sheet card card--front" aria-label="Business card front">
  <svg class="fan" width="260" height="150" viewBox="0 0 260 150" role="img" aria-label="Soft fan of translucent warm and cool shards spreading from the top right corner">
    <defs>
      <linearGradient id="fanCard" x1="0" y1="0" x2="1" y2="1">
        <stop offset="0" stop-color="var(--fan-warm)" stop-opacity="0.7"/>
        <stop offset="1" stop-color="var(--fan-cool)" stop-opacity="0.3"/>
      </linearGradient>
    </defs>
    <polygon points="260,0 40,0 90,150 260,70" fill="url(#fanCard)" opacity="0.6"/>
  </svg>
  <div class="brand">
    <span class="brand__mark"></span>
    <p class="brand__name">Halbrook Marsh</p>
    <p class="brand__tagline">Commercial Real Estate</p>
  </div>
  <p class="web">www.halbrookmarshrealestate.com</p>
  <div class="person">
    <p class="person__name">Name Surname</p>
    <p class="person__role">Marketing Manager</p>
  </div>
  <dl class="contact">
    <dt>Mobile:</dt><dd>(01) 12345678</dd>
    <dt>Tel:</dt><dd>(01) 12345678</dd>
    <dt>email:</dt><dd>email@halbrookmarsh.com</dd>
    <dt>Address:</dt><dd>Address name 1234Address line 2 01234<br>State, Region, Country</dd>
  </dl>
</section>

</body>
</html>
```